Design Guideline for an Overview Graphic
Title: Circular Economy & Future Business Models
Objective: Summarize key innovation fields, business models, and sustainability opportunities for Voltara AG in the circular economy.

1. Structure & Layout
A. Circular Economy Principles (Top Section / Centerpiece)
Goal: Introduce the fundamentals of circular economy in a visually engaging way.
πŸ”Ή Reduce β†’ Minimize resource usage
πŸ”Ή Reuse β†’ Extend product lifecycles
πŸ”Ή Recycle β†’ Reintegrate materials into production
πŸ–ŒοΈ Design Suggestion:
β€’ A circular flowchart with three interconnected icons (one for each principle).
β€’ Arrows connecting them to show the cyclical nature.

B. Key Innovation Fields (Main Body – 5 Thematic Blocks)
Each block represents a strategic business opportunity in the circular economy.

1st Circular Material Use in Waste & Water Management
πŸ“Œ Key Innovations:
βœ… Urban Mining (Extracting raw materials from waste)
β€’ Example: Brenvika Recycling
βœ… Water Recycling & Reuse
β€’ Industrial wastewater treatment
β€’ Example: Quenset Water Technologies
βœ… Biomass for Energy Generation
β€’ Organic waste to biofuel
β€’ Example: KΓΌsnacht biogas plant
β€’ Icons for waste, water, and biomass
β€’ Infographic-style arrows connecting waste to usable resources

2. Circular Energy Use & Storage Technologies
πŸ“Œ Key Innovations:
βœ… Second-Life Batteries
β€’ EV batteries reused as stationary storage
β€’ Example: Talvo yCell
βœ… Hydrogen Economy
β€’ Power-to-gas technology
β€’ Example: Parvix Transit Germany
βœ… Industrial Waste Heat Recovery
β€’ Reusing waste heat for energy
β€’ Example: Ardis Waste Heat Recovery
β€’ Battery, hydrogen, and heat recovery icons
β€’ Use energy flow arrows to show repurposing

3. As-a-Service Models for Sustainability
πŸ“Œ Key Innovations:
βœ… Heat-as-a-Service (Leased heating solutions)
β€’ Example: Korblund Heizung
βœ… Water as a Service (Industrial water management)
β€’ Example: Brovi
βœ… Zero-waste logistics for companies
β€’ Material return & reuse services
β€’ Example: Dask by QuillaPax
β€’ Modular grid design with icons & short descriptions
β€’ Flowchart representation of the service process

4th ICT & AI for Circular Economy
πŸ“Œ Key Innovations:
βœ… Digital Platforms for Resource Sharing
β€’ Example: Navtrex (Plastics Marketplace)
βœ… AI-Based Waste Sorting
β€’ Machine learning-driven waste classification
β€’ Example: Zelko Robotics
βœ… IoT for Water Management
β€’ Real-time leak detection
β€’ Example: Falbrook Electric Water Management
β€’ Icons for AI, IoT, and digital platforms
β€’ Tech-style visualization (data points, connections, automation lines)

```html
<!DOCTYPE html>
<html lang="en">
<head>
<meta charset="utf-8">
<title>Circular Economy &amp; Future Business Models – Voltara AG</title>
<link href="https://fonts.googleapis.com/css2?family=Poppins:wght@400;500;700;800&display=swap" rel="stylesheet">
<style>
:root{
  --bg:#f5f6f7;
  --halo-outer:#e8eaec;
  --halo-inner:#d6d8db;
  --red-head:#bf2536;
  --red:#e03a47;
  --navy-head:#053c68;
  --navy:#07528a;
  --violet-head:#6426df;
  --violet:#7b46f0;
  --teal-head:#1aa0ad;
  --teal:#1fc8d6;
  --reduce:#38b0de;
  --reduce-ring:#1e9fd8;
  --reuse:#fb8c1f;
  --reuse-ring:#ff7a0a;
  --recycle:#98c000;
  --recycle-ring:#8aab12;
  --core:#ffd24d;
  --core-ring:#dcdde0;
  --dots:#0b1f33;
  --white:#ffffff;
}
*{box-sizing:border-box;margin:0;padding:0}
html,body{width:1200px;height:942px;overflow:hidden;background:var(--bg)}
body{font-family:"Poppins",sans-serif;color:var(--white);position:relative}
.stage{position:absolute;inset:0;width:1200px;height:942px}

.panel{position:absolute;overflow:hidden}
.panel__head{position:absolute;left:0;right:0;top:0;height:31px;display:flex;align-items:center;justify-content:center;font-weight:700;font-size:11.4px;letter-spacing:-.1px}
.panel__label{position:absolute;left:0;right:0;text-align:center;font-weight:700;font-size:9.4px}
.panel__label span{border-bottom:1px solid var(--white);padding-bottom:1px}
.ico{position:absolute;width:33px;height:33px}
.txt{position:absolute;font-size:9.4px;line-height:13.7px;font-weight:400}
.txt b{font-weight:700}
.rule{position:absolute;width:1px;background:rgba(255,255,255,.55)}

.panel--waste{left:396px;top:77px;width:408px;height:182px;background:var(--red);
  clip-path:polygon(0 0,390px 0,408px 31px,408px 182px,18px 182px,0 155px)}
.panel--waste .panel__head{background:var(--red-head)}
.panel--energy{left:96px;top:374px;width:290px;height:194px;background:var(--navy);
  clip-path:polygon(0 0,272px 0,290px 31px,290px 194px,18px 194px,0 164px)}
.panel--energy .panel__head{background:var(--navy-head)}
.panel--service{left:813px;top:374px;width:290px;height:194px;background:var(--violet);
  clip-path:polygon(0 0,272px 0,290px 31px,290px 194px,18px 194px,0 164px)}
.panel--service .panel__head{background:var(--violet-head)}
.panel--digital{left:392px;top:682px;width:416px;height:182px;background:var(--teal);
  clip-path:polygon(18px 0,416px 0,416px 150px,398px 182px,0 182px,0 32px)}
.panel--digital .panel__head{background:var(--teal-head);height:32px}

.cycle-label{position:absolute;font-size:9.4px;line-height:16px;font-weight:400}
.cycle-label h3{font-size:14.5px;font-weight:800;line-height:18px;display:inline-block;border-bottom:1.5px solid var(--white);margin-bottom:2px}
.core-title{position:absolute;left:531px;top:446px;width:138px;text-align:center;font-weight:800;font-size:14px;line-height:25px;letter-spacing:.3px}
</style>
</head>
<body>
<main class="stage">

<svg class="backdrop" width="1200" height="942" viewBox="0 0 1200 942" aria-hidden="true" style="position:absolute;left:0;top:0">
  <circle cx="600" cy="471" r="413" fill="var(--halo-outer)"/>
  <circle cx="600" cy="471" r="342" fill="var(--halo-inner)"/>

  <g fill="none" stroke="var(--dots)" stroke-width="2.4" stroke-dasharray="0.1 4.4" stroke-linecap="round">
    <path d="M380 166 H299 V262 L429 362"/>
    <path d="M243 580 V606 H452"/>
    <path d="M958 580 V606 H750"/>
    <path d="M721 672 V628"/>
  </g>
  <g fill="var(--dots)">
    <circle cx="380" cy="166" r="4"/><circle cx="243" cy="580" r="4"/>
    <circle cx="958" cy="580" r="4"/><circle cx="721" cy="672" r="4"/>
  </g>

  <g class="cycle">
    <circle cx="600" cy="471" r="196" fill="none" stroke="var(--white)" stroke-width="6"/>
    <path d="M416 545 A196 196 0 0 1 594 275" fill="none" stroke="var(--reduce-ring)" stroke-width="2.2"/>
    <path d="M594 275 A196 196 0 0 1 759 586" fill="none" stroke="var(--reuse-ring)" stroke-width="2.2"/>
    <path d="M759 586 A196 196 0 0 1 416 545" fill="none" stroke="var(--recycle-ring)" stroke-width="2.2"/>

    <path d="M416.8 503.4 A186 186 0 0 1 663.6 296.2 L678.3 355 L632.5 381.7 A95 95 0 0 0 506.4 487.5 L460.3 461.2 Z" fill="var(--reduce)"/>
    <path d="M663.6 296.2 A186 186 0 0 1 719.6 613.5 L661.3 596.9 L661.1 543.8 A95 95 0 0 0 632.5 381.7 L678.3 355 Z" fill="var(--reuse)"/>
    <path d="M719.6 613.5 A186 186 0 0 1 416.8 503.4 L460.3 461.2 L506.4 487.5 A95 95 0 0 0 661.1 543.8 L661.3 596.9 Z" fill="var(--recycle)"/>

    <circle cx="600" cy="471" r="94" fill="none" stroke="rgba(0,0,0,.12)" stroke-width="8"/>
    <circle cx="600" cy="471" r="89" fill="var(--core-ring)"/>
    <circle cx="600" cy="473" r="70" fill="rgba(0,0,0,.12)"/>
    <circle cx="600" cy="471" r="69" fill="var(--core)"/>
  </g>

  <g class="badge badge--reduce">
    <circle cx="467" cy="339" r="25" fill="var(--white)" stroke="rgba(0,0,0,.08)"/>
    <path d="M451 336 Q462 346 477 339" fill="none" stroke="var(--reduce-ring)" stroke-width="4" stroke-linecap="round"/>
    <path d="M472 331 L483 339 L471 346 Z" fill="var(--reduce-ring)"/>
  </g>
  <g class="badge badge--reuse">
    <circle cx="779" cy="420" r="25" fill="var(--white)" stroke="rgba(0,0,0,.08)"/>
    <path d="M767 426 A12 12 0 0 1 786 410" fill="none" stroke="var(--reuse-ring)" stroke-width="4.5" stroke-linecap="round"/>
    <path d="M791 414 A12 12 0 0 1 772 430" fill="none" stroke="var(--reuse-ring)" stroke-width="4.5" stroke-linecap="round"/>
    <path d="M783 404 L792 408 L784 415 Z M775 436 L766 432 L774 425 Z" fill="var(--reuse-ring)"/>
  </g>
  <g class="badge badge--recycle">
    <circle cx="553" cy="651" r="25" fill="var(--white)" stroke="rgba(0,0,0,.08)"/>
    <g fill="none" stroke="var(--recycle)" stroke-width="4.2" stroke-linejoin="round">
      <path d="M547 644 L553 635 L560 645"/>
      <path d="M563 651 L567 658 L555 659"/>
      <path d="M549 659 L539 659 L543 651"/>
    </g>
  </g>
</svg>

<!-- cycle labels -->
<div class="cycle-label" style="left:453px;top:381px"><h3>REDUCE</h3><br>Minimize<br>resource<br>usage</div>
<div class="cycle-label" style="left:703px;top:391px"><h3>REUSE</h3><br>Extend<br>product<br>lifecycles</div>
<div class="cycle-label" style="left:574px;top:575px"><h3>RECYCLE</h3><br>Reintegrate materials<br>into production</div>
<div class="core-title">USABLE<br>RESOURCES</div>

<!-- 1st panel -->
<section class="panel panel--waste">
  <div class="panel__head">1st Circular Material Use in Waste &amp; Water Management</div>
  <div class="panel__label" style="top:32px"><span>Key Innovations:</span></div>
  <svg class="ico" style="left:11px;top:53px" viewBox="0 0 32 32" aria-hidden="true"><circle cx="16" cy="16" r="16" fill="#fff"/><path d="M10 11 H22 L20.5 24 H11.5 Z M9 11 H23 M13.5 11 V8.5 H18.5 V11" fill="none" stroke="var(--red)" stroke-width="1.8" stroke-linejoin="round"/></svg>
  <svg class="ico" style="left:140px;top:53px" viewBox="0 0 32 32" aria-hidden="true"><circle cx="16" cy="16" r="16" fill="#fff"/><circle cx="16" cy="16" r="11" fill="none" stroke="var(--red)" stroke-width="2" stroke-dasharray="15 3"/><path d="M16 10 Q20.5 16 20 18.5 A4 4 0 0 1 12 18.5 Q11.5 16 16 10 Z" fill="var(--red)"/></svg>
  <svg class="ico" style="left:272px;top:53px" viewBox="0 0 32 32" aria-hidden="true"><circle cx="16" cy="16" r="16" fill="#fff"/><path d="M16 7 A6 6 0 0 1 19.5 17.5 V20 H12.5 V17.5 A6 6 0 0 1 16 7 Z M13 22.5 H19 M9 25 Q12 21 15 24 M23 25 Q20 21 17 24" fill="none" stroke="var(--red)" stroke-width="1.5" stroke-linecap="round"/><path d="M16.8 10 L14.5 14 H17.2 L15.2 17.5" fill="none" stroke="var(--red)" stroke-width="1.3"/></svg>
  <div class="rule" style="left:130px;top:54px;height:104px"></div>
  <div class="rule" style="left:260px;top:54px;height:104px"></div>
  <div class="txt" style="left:10px;top:90px;width:118px"><b>Urban Mining</b><br>(Extracting raw materials from&nbsp; waste)<br>• Example:<br>Brenvika Recycling</div>
  <div class="txt" style="left:138px;top:90px;width:122px"><b>Water Recycling &amp; Reuse</b><br>• Industrial wastewater treatment<br>• Example: Quenset Water Technologies</div>
  <div class="txt" style="left:271px;top:90px;width:134px"><b>Biomass for Energy Generation</b><br>• Organic waste to biofuel<br>• Example: Lindrach biogas plant</div>
</section>

<!-- 2nd panel -->
<section class="panel panel--energy">
  <div class="panel__head">Circular Energy Use &amp; Storage Technologies</div>
  <div class="panel__label" style="top:32px"><span>Key Innovations:</span></div>
  <svg class="ico" style="left:13px;top:56px" viewBox="0 0 32 32" aria-hidden="true"><circle cx="16" cy="16" r="16" fill="#fff"/><rect x="7" y="11" width="16" height="10" rx="2" fill="none" stroke="var(--navy)" stroke-width="2.2"/><rect x="23.5" y="14" width="2" height="4" fill="var(--navy)"/><path d="M11 14 V18 M15 14 V18 M19 14 V18" stroke="var(--navy)" stroke-width="2"/></svg>
  <svg class="ico" style="left:13px;top:100px" viewBox="0 0 32 32" aria-hidden="true"><circle cx="16" cy="16" r="16" fill="#fff"/><circle cx="19" cy="12.5" r="6.5" fill="var(--navy)"/><circle cx="12" cy="20" r="6.5" fill="none" stroke="var(--navy)" stroke-width="1.6"/><text x="19" y="14.8" font-size="6" font-family="Poppins,sans-serif" font-weight="700" fill="#fff" text-anchor="middle">H</text><text x="12" y="22.3" font-size="6" font-family="Poppins,sans-serif" font-weight="700" fill="var(--navy)" text-anchor="middle">H</text></svg>
  <svg class="ico" style="left:13px;top:144px" viewBox="0 0 32 32" aria-hidden="true"><circle cx="16" cy="16" r="16" fill="#fff"/><rect x="9" y="9" width="14" height="14" rx="2" fill="var(--navy)"/><path d="M11 6 V9 M16 6 V9 M21 6 V9 M11 23 V26 M16 23 V26 M21 23 V26 M6 11 H9 M6 16 H9 M6 21 H9 M23 11 H26 M23 16 H26 M23 21 H26" stroke="var(--navy)" stroke-width="1.5"/><path d="M16 11.5 Q19.5 15 19 18 A3 3 0 0 1 13 18 Q13 15.5 16 11.5 Z" fill="#fff"/></svg>
  <div class="txt" style="left:57px;top:52px;width:230px"><b>Second-Life Batteries</b><br>• EV batteries reused as stationary storage<br>• Example: Talvo yCell</div>
  <div class="txt" style="left:57px;top:95px;width:230px"><b>Hydrogen Economy</b><br>• Power-to-gas technology<br>• Example: Parvix Transit Germany</div>
  <div class="txt" style="left:57px;top:139px;width:230px"><b>Industrial Waste Heat Recovery</b><br>• Reusing waste heat for energy<br>• Example: Ardis Waste Heat Recovery</div>
</section>

<!-- 3rd panel -->
<section class="panel panel--service">
  <div class="panel__head">As-a-Service Models for Sustainability</div>
  <div class="panel__label" style="top:32px"><span>Key Innovations:</span></div>
  <svg class="ico" style="left:10px;top:56px" viewBox="0 0 32 32" aria-hidden="true"><circle cx="16" cy="16" r="16" fill="#fff"/><rect x="9" y="15" width="12" height="8" rx="1.5" fill="var(--violet)"/><path d="M5 19 H9 M21 19 H25 M23 8 V15" stroke="var(--violet)" stroke-width="1.6"/><circle cx="23" cy="16" r="1.8" fill="var(--violet)"/><path d="M15.5 16.5 L13.5 19.5 H16 L14.5 22" stroke="#fff" stroke-width="1.2" fill="none"/></svg>
  <svg class="ico" style="left:10px;top:100px" viewBox="0 0 32 32" aria-hidden="true"><circle cx="16" cy="16" r="16" fill="#fff"/><circle cx="16" cy="16" r="9" fill="none" stroke="var(--violet)" stroke-width="3" stroke-dasharray="3 2.2"/><circle cx="16" cy="16" r="6" fill="none" stroke="var(--violet)" stroke-width="1.4"/><path d="M16 12 Q18.5 15.5 18 17 A2 2 0 0 1 14 17 Q13.5 15.5 16 12 Z" fill="var(--violet)"/></svg>
  <svg class="ico" style="left:10px;top:144px" viewBox="0 0 32 32" aria-hidden="true"><circle cx="16" cy="16" r="16" fill="#fff"/><circle cx="16" cy="16" r="10.5" fill="none" stroke="var(--violet)" stroke-width="1.4" stroke-dasharray="14 3"/><text x="16" y="15.3" font-size="5" font-family="Poppins,sans-serif" font-weight="700" fill="var(--violet)" text-anchor="middle">ZERO</text><text x="16" y="20.5" font-size="4.6" font-family="Poppins,sans-serif" font-weight="700" fill="var(--violet)" text-anchor="middle">WASTE</text></svg>
  <div class="txt" style="left:50px;top:58px;width:240px"><b>Heat-as-a-Service</b> (Leased heating solutions)<br>• Example: Korblund Heizung</div>
  <div class="txt" style="left:50px;top:101px;width:240px"><b>Water as a Service</b> (Industrial water management)<br>• Example: Brovi</div>
  <div class="txt" style="left:50px;top:136px;width:240px;line-height:16px"><b>Zero-waste logistics for companies</b><br>• Material return &amp; reuse services<br>• Example: Dask by QuillaPax</div>
</section>

<!-- 4th panel -->
<section class="panel panel--digital">
  <div class="panel__head">4th ICT &amp; AI for Circular Economy</div>
  <div class="panel__label" style="top:32px"><span>Key Innovations:</span></div>
  <svg class="ico" style="left:11px;top:53px" viewBox="0 0 32 32" aria-hidden="true"><circle cx="16" cy="16" r="16" fill="#fff"/><circle cx="16" cy="16" r="6" fill="none" stroke="var(--teal)" stroke-width="1.6"/><path d="M16 10 V6 M22 16 H26 M16 22 V26 M10 16 H6 M20 12 L23.5 8.5 M12 20 L8.5 23.5 M20 20 L23.5 23.5 M12 12 L8.5 8.5" stroke="var(--teal)" stroke-width="1.4"/><circle cx="16" cy="16" r="2" fill="var(--teal)"/></svg>
  <svg class="ico" style="left:140px;top:53px" viewBox="0 0 32 32" aria-hidden="true"><circle cx="16" cy="16" r="16" fill="#fff"/><circle cx="16" cy="16" r="8" fill="var(--teal-head)"/><path d="M16 5 V8 M16 24 V27 M5 16 H8 M24 16 H27 M11 7 V9 M21 7 V9 M11 23 V25 M21 23 V25" stroke="var(--teal-head)" stroke-width="1.5"/><text x="16" y="18.3" font-size="6.4" font-family="Poppins,sans-serif" font-weight="700" fill="#fff" text-anchor="middle">AI</text></svg>
  <svg class="ico" style="left:273px;top:53px" viewBox="0 0 32 32" aria-hidden="true"><circle cx="16" cy="16" r="16" fill="#fff"/><path d="M16 6 Q21.5 13 21 16 A5 5 0 0 1 11 16 Q10.5 13 16 6 Z" fill="none" stroke="var(--teal)" stroke-width="1.5"/><path d="M6 22 H11 Q13 22 15 24 H20 M6 26 H22 L26 22" fill="none" stroke="var(--teal)" stroke-width="1.5" stroke-linecap="round"/></svg>
  <div class="rule" style="left:131px;top:53px;height:107px"></div>
  <div class="rule" style="left:266px;top:53px;height:107px"></div>
  <div class="txt" style="left:11px;top:89px;width:118px;line-height:16px"><b>Digital Platforms for Resource Sharing</b><br>• Example: Navtrex (Plastics Marketplace)</div>
  <div class="txt" style="left:141px;top:89px;width:125px;line-height:16px"><b>AI-Based Waste Sorting</b><br>• Machine learning-driven waste classification<br>• Example: Zelko Robotics</div>
  <div class="txt" style="left:273px;top:90px;width:140px"><b>IoT for Water Management</b><br>• Real-time leak detection<br>• Example: Falbrook Electric Water Management</div>
</section>

</main>
</body>
</html>
```